Estate Planning Law Firm opening new branch in Florida

I am an experienced estate planning attorney that recently relocated to Florida. Looking for a banner Ad to place on platforms such as YardLoop, Chatterly and Pixmora to create publicity for firm and new leads.

```html
<!DOCTYPE html>
<html lang="en">
<head>
<meta charset="utf-8">
<title>Serenova Law Firm – Welcome Banner</title>
<link href="https://fonts.googleapis.com/css2?family=Cinzel:wght@500;700;800&family=Fira+Sans:wght@400;500&display=swap" rel="stylesheet">
<style>
  :root{
    --ink:#2a394b;
    --navy-panel:#2b3a4c;
    --teal:#1d6f86;
    --teal-mark:#1f7a74;
    --text:#141414;
    --paper:#ffffff;
  }
  *{box-sizing:border-box;margin:0;padding:0}
  html,body{width:1200px;height:628px;overflow:hidden;background:var(--paper)}
  .banner{position:relative;width:1200px;height:628px;background:var(--paper);overflow:hidden}
  .side-panel{position:absolute;left:851px;top:0;width:349px;height:628px;background:var(--navy-panel)}
  .photo{
    position:absolute;left:600px;top:40px;width:562px;height:548px;
    background:linear-gradient(180deg,#3f8fd6 0%,#7fb7e6 22%,#c9d6dc 32%,#8d9ea6 42%,#2f8fa6 55%,#2b8aa0 68%,#3f7a3a 80%,#2f5e2a 100%);
  }
  .brand-column{position:absolute;left:0;top:0;width:622px;text-align:center}
  .brand{
    position:absolute;left:128px;top:52px;display:flex;align-items:center;gap:16px;
  }
  .brand-square{width:52px;height:52px;background:var(--teal-mark)}
  .brand-text{display:flex;flex-direction:column;align-items:center}
  .brand-name{font-family:'Cinzel',serif;font-weight:500;font-size:50px;line-height:1;color:var(--ink);letter-spacing:1px}
  .brand-sub{
    display:flex;align-items:center;gap:10px;margin-top:10px;
    font-family:'Fira Sans',sans-serif;font-size:17px;letter-spacing:1px;color:var(--ink)
  }
  .brand-sub::before,.brand-sub::after{content:"";width:56px;height:1.5px;background:var(--teal-mark)}
  .headline{
    position:absolute;left:0;top:160px;width:622px;
    font-family:'Cinzel',serif;font-weight:800;font-size:56px;line-height:72px;color:var(--ink);letter-spacing:1px
  }
  .services{position:absolute;left:0;top:312px;width:622px;font-family:'Fira Sans',sans-serif;font-size:20px;color:var(--text)}
  .rule{position:absolute;left:237px;top:368px;width:148px;height:5px;background:var(--teal)}
  .social{position:absolute;left:219px;top:410px;display:flex;gap:11px;list-style:none}
  .social li{width:54px;height:54px;border-radius:50%;background:var(--teal)}
  .contact{position:absolute;left:0;width:622px;font-family:'Fira Sans',sans-serif;font-size:25px;color:var(--text)}
  .contact.phone{top:502px}
  .contact.email{top:550px}
</style>
</head>
<body>
  <div class="banner">
    <div class="side-panel"></div>
    <div class="photo" role="img" aria-label="Aerial photo of a Florida city skyline around a lake with a fountain, surrounded by trees under a blue sky"></div>

    <div class="brand-column">
      <div class="brand">
        <span class="brand-square"></span>
        <div class="brand-text">
          <span class="brand-name">SERENOVA</span>
          <span class="brand-sub">LAW FIRM, PLLC</span>
        </div>
      </div>

      <h1 class="headline">WELCOME TO<br>SERENOVA</h1>
      <p class="services">Estate Planning &amp; Financial Planning</p>
      <div class="rule"></div>

      <ul class="social" aria-label="Social links">
        <li aria-label="Chatterly"></li>
        <li aria-label="Linkora"></li>
        <li aria-label="News feed"></li>
      </ul>

      <p class="contact phone">Phone Call: (321) 555-0147</p>
      <p class="contact email">Send Email: hello@serenova.law</p>
    </div>
  </div>
</body>
</html>
```